Clean Plinth Ads Banner Design For A Finance Company

Hi,
We're a UK based finance company and are looking for new banner ads to use on the Plinth Display Network.
We want the end product to stand out by using strong, minimal design - ideally starting from a dark theme, although I'm open to ideas.
The copy should read:
'Fast Bridging Loans From 0.39% PM'
Once we have these designs agreed, we are looking to replicate them for other products, changing only the text on each ad - for example, 'commercial mortgage service you can rely on' or 'development finance service you can rely on'.
The colours used on our website are the following:
Black - #040303
Orange - #f79124
White - #ffffff
Grey - #ffffff
Example ads that I like - https://www.brimcastle.com/wp-content/uploads/2021/07/plinth-display-ads-example-2-final.png.webp
2 - https://quendrahub.com/wp-content/uploads/2020/03/fbdd56ba3bd16c7a8debb13a411de786.jpg

```html
<!DOCTYPE html>
<html lang="en">
<head>
<meta charset="utf-8">
<title>Corvell Finance – Bridging Loan Banner Set</title>
<link rel="stylesheet" href="https://fonts.googleapis.com/css2?family=Poppins:wght@400;500;600;700;800&family=Montserrat:wght@400;500&display=swap">
<style>
  :root{
    --stage:#e4e4e4;
    --panel:#221e1e;
    --orange:#f79124;
    --white:#ffffff;
    --muted:#d9d9d9;
    --photo-a:#c9cdd4;
    --photo-b:#8d97a5;
  }
  *{box-sizing:border-box;margin:0;padding:0}
  html,body{width:1200px;height:743px;overflow:hidden;background:var(--stage)}
  body{position:relative;font-family:"Poppins",sans-serif;color:var(--white)}

  .banner{position:absolute;background:var(--panel);overflow:hidden}

  /* shared pieces */
  .brand{color:var(--orange);font-weight:700;line-height:1;text-align:center}
  .brand-name{display:block;font-size:2.3em;letter-spacing:-.01em}
  .brand-sub{display:block;font-size:.78em;margin-top:.2em;color:var(--white);font-weight:400}
  .brand-sub b{font-weight:700}
  .photo{border-radius:50%;border:.35em solid var(--orange);background:radial-gradient(circle at 45% 40%,var(--photo-a),var(--photo-b));flex:none}
  .headline{font-weight:800;text-transform:uppercase;line-height:1.05;text-align:center;font-size:var(--h,1.5em)}
  .headline em{font-style:normal;color:var(--orange)}
  .pill{background:var(--orange);color:var(--white);border-radius:1em;padding:.15em .9em;font-size:.9em;line-height:1.2;text-align:center}
  .copy{font-family:"Montserrat",sans-serif;font-size:.6em;letter-spacing:.05em;text-align:center;line-height:1.3;color:var(--muted)}
  .rule{display:flex;gap:.25em}
  .rule i{display:block;height:.18em;width:2.2em;background:var(--orange)}
  .rule i+i{width:1em;background:var(--white)}
  .call{font-size:.75em;text-align:center;line-height:1.2}
  .phone{display:block;color:var(--orange);font-weight:600;font-size:1.3em}
  .web{font-family:"Montserrat",sans-serif;font-size:.8em;letter-spacing:.35em;text-align:center}
  .web b{color:var(--orange);font-weight:400}
  .cta{display:inline-flex;align-items:center;gap:.6em;background:var(--orange);border-radius:2em;padding:.4em .5em .4em 1.4em;font-size:.6em;font-weight:700;letter-spacing:.15em}
  .cta svg{width:1.6em;height:1.6em}
  .arrows{position:absolute;height:.9em;width:3em}
  .arrows.in-flow{position:static;flex:none}

  /* vertical formats */
  .stack{display:flex;flex-direction:column;align-items:center;justify-content:space-between}

  .tall{left:69px;top:87px;width:237px;height:473px;font-size:10px;padding:24px 0 22px}
  .tall .photo{width:236px;height:236px;margin-top:4px}
  .tall .headline{--h:1.5em}

  .square{left:638px;top:87px;width:197px;height:197px;font-size:7px;padding:8px 0 9px}
  .square .photo{width:98px;height:98px}
  .square .headline{--h:1.45em}
  .square .brand-name{font-size:1.7em}

  .rect-lg{left:329px;top:339px;width:265px;height:221px;font-size:7.5px;padding:8px 0 8px}
  .rect-lg .photo{width:108px;height:108px}
  .rect-lg .headline{--h:1.5em}
  .rect-lg .brand-name{font-size:1.7em}

  .rect-md{left:618px;top:363px;width:237px;height:197px;font-size:7px;padding:9px 0 9px}
  .rect-md .photo{width:98px;height:98px}
  .rect-md .headline{--h:1.4em}
  .rect-md .brand-name{font-size:1.7em}

  .sky{left:877px;top:87px;width:127px;height:473px;font-size:8px;padding:48px 6px 26px}
  .sky .photo{width:127px;height:127px}
  .sky .headline{--h:1.9em}
  .sky .copy{font-size:.95em}

  .sky-narrow{left:1036px;top:87px;width:95px;height:473px;font-size:7px;padding:50px 4px 56px}
  .sky-narrow .photo{width:95px;height:95px}
  .sky-narrow .headline{--h:1.95em}
  .sky-narrow .copy{font-size:.95em}
  .sky-narrow .brand-name{font-size:2em}

  /* horizontal formats */
  .strip{display:flex;align-items:center}
  .strip .text{display:flex;flex-direction:column;align-items:center;gap:.3em}
  .strip .call{text-align:right}

  .leader-sm{left:335px;top:146px;width:252px;height:80px;font-size:5.5px;padding:0 6px 0 16px;gap:4px}
  .leader-sm .photo{width:46px;height:46px}
  .leader-sm .headline{--h:1.6em}
  .leader-sm .brand-name{font-size:2.2em}
  .leader-sm .call{position:absolute;right:8px;bottom:7px;font-size:.8em}

  .leader-lg{left:69px;top:584px;width:575px;height:72px;font-size:7.5px;padding:0 10px 0 70px;gap:14px}
  .leader-lg .photo{width:68px;height:68px}
  .leader-lg .headline{--h:2.1em}
  .leader-lg .brand-name{font-size:3.3em}
  .leader-lg .text{flex:1}

  .leader-md{left:691px;top:598px;width:369px;height:48px;font-size:5px;padding:0 8px 0 36px;gap:8px}
  .leader-md .photo{width:46px;height:46px}
  .leader-md .headline{--h:2.2em}
  .leader-md .brand-name{font-size:3.2em}
  .leader-md .text{flex:1}
</style>
</head>
<body>

<svg width="0" height="0" style="position:absolute" aria-hidden="true">
  <defs>
    <symbol id="tri-arrows" viewBox="0 0 30 9"><path d="M0 0l7 4.5L0 9zM11 0l7 4.5L11 9z" fill="#fff"/><path d="M22 0l7 4.5L22 9z" fill="#f79124"/></symbol>
    <symbol id="play" viewBox="0 0 16 16"><circle cx="8" cy="8" r="7" fill="none" stroke="#fff" stroke-width="1.6"/><path d="M6.5 5l4 3-4 3z" fill="#fff"/></symbol>
  </defs>
</svg>

<!-- 240x480 style -->
<section class="banner tall stack">
  <div class="brand"><span class="brand-name">Corvell</span><span class="brand-sub"><b>Finance</b> Limited</span></div>
  <div class="photo" role="img" aria-label="Photo of a finance adviser with a couple reviewing a laptop"></div>
  <svg class="arrows in-flow" style="align-self:flex-start;margin-left:19px;font-size:10px"><use href="#tri-arrows"/></svg>
  <h2 class="headline">Bridging Loan <em>Service</em></h2>
  <p class="pill">5 Star Rated Service &amp; No Broker Fees</p>
  <p class="copy">'Commercial Mortgage Service You Can Rel On' Or<br>'Development Finance Service</p>
  <div class="rule"><i></i><i></i></div>
  <p class="call">CALL NOW:-<span class="phone">0800-555-0147</span></p>
  <p class="web">www.<b>corvell</b>.co.uk</p>
  <span class="cta">CLICK HERE<svg><use href="#play"/></svg></span>
  <svg class="arrows" style="left:175px;top:508px;font-size:8px"><use href="#tri-arrows"/></svg>
</section>

<!-- small leaderboard -->
<section class="banner leader-sm strip">
  <div class="brand"><span class="brand-name">Corvell</span><span class="brand-sub"><b>Finance</b> Limited</span></div>
  <div class="photo" role="img" aria-label="Photo of a finance adviser with a couple reviewing a laptop"></div>
  <div class="text">
    <h2 class="headline">Bridging Loan <em>Service</em></h2>
    <p class="pill">5 Star Rated Service &amp; No Broker Fees</p>
    <p class="copy">'Commercial Mortgage Service You Can Rel On' Or<br>'Development Finance Service</p>
    <p class="web">www.<b>corvell</b>.co.uk</p>
    <span class="cta">CLICK HERE<svg><use href="#play"/></svg></span>
  </div>
  <p class="call">CALL NOW:-<span class="phone">0800-555-0147</span></p>
  <svg class="arrows" style="left:10px;bottom:8px;font-size:6px"><use href="#tri-arrows"/></svg>
  <svg class="arrows" style="right:12px;top:10px;font-size:5px"><use href="#tri-arrows"/></svg>
</section>

<!-- square -->
<section class="banner square stack">
  <div class="brand"><span class="brand-name">Corvell</span><span class="brand-sub"><b>Finance</b> Limited</span></div>
  <div class="photo" role="img" aria-label="Photo of a finance adviser with a couple reviewing a laptop"></div>
  <h2 class="headline">Bridging Loan <em>Service</em></h2>
  <p class="pill">5 Star Rated Service &amp; No Broker Fees</p>
  <p class="copy">'Commercial Mortgage Service You Can Rel On' Or<br>'Development Finance Service</p>
  <div class="rule"><i></i><i></i></div>
  <p class="call">CALL NOW:-<span class="phone">0800-555-0147</span></p>
  <p class="web">www.<b>corvell</b>.co.uk</p>
  <svg class="arrows" style="left:16px;top:120px;font-size:5px"><use href="#tri-arrows"/></svg>
  <span class="cta" style="position:absolute;right:16px;bottom:12px;font-size:3px">CLICK HERE<svg><use href="#play"/></svg></span>
</section>

<!-- medium rectangle -->
<section class="banner rect-lg stack">
  <div class="brand"><span class="brand-name">Corvell</span><span class="brand-sub"><b>Finance</b> Limited</span></div>
  <div class="photo" role="img" aria-label="Photo of a finance adviser with a couple reviewing a laptop"></div>
  <h2 class="headline">Bridging Loan <em>Service</em></h2>
  <p class="pill">5 Star Rated Service &amp; No Broker Fees</p>
  <p class="copy">'Commercial Mortgage Service You Can Rel On' Or<br>'Development Finance Service</p>
  <div class="rule"><i></i><i></i></div>
  <p class="call">CALL NOW:-<span class="phone">0800-555-0147</span></p>
  <p class="web">www.<b>corvell</b>.co.uk</p>
  <svg class="arrows" style="left:30px;top:130px;font-size:5px"><use href="#tri-arrows"/></svg>
  <svg class="arrows" style="right:38px;top:177px;font-size:7px"><use href="#tri-arrows"/></svg>
  <span class="cta" style="position:absolute;right:18px;bottom:10px;font-size:3.5px">CLICK HERE<svg><use href="#play"/></svg></span>
</section>

<!-- rectangle -->
<section class="banner rect-md stack">
  <div class="brand"><span class="brand-name">Corvell</span><span class="brand-sub"><b>Finance</b> Limited</span></div>
  <div class="photo" role="img" aria-label="Photo of a finance adviser with a couple reviewing a laptop"></div>
  <h2 class="headline">Bridging Loan <em>Service</em></h2>
  <p class="pill">5 Star Rated Service &amp; No Broker Fees</p>
  <p class="copy">'Commercial Mortgage Service You Can Rel On' Or<br>'Development Finance Service</p>
  <div class="rule"><i></i><i></i></div>
  <p class="call">CALL NOW:-<span class="phone">0800-555-0147</span></p>
  <p class="web">www.<b>corvell</b>.co.uk</p>
  <svg class="arrows" style="left:36px;top:115px;font-size:5px"><use href="#tri-arrows"/></svg>
  <span class="cta" style="position:absolute;right:26px;bottom:12px;font-size:3.2px">CLICK HERE<svg><use href="#play"/></svg></span>
</section>

<!-- skyscraper -->
<section class="banner sky stack">
  <div class="brand"><span class="brand-name">Corvell</span><span class="brand-sub"><b>Finance</b> Limited</span></div>
  <div class="photo" role="img" aria-label="Photo of a finance adviser with a couple reviewing a laptop"></div>
  <h2 class="headline">Bridging<br>Loan<br><em>Service</em></h2>
  <p class="pill">5 Star Rated Service<br>&amp; No Broker Fees</p>
  <p class="copy">'Commercial Mortgage<br>Service You Can<br>Rel On' Or<br>'Development<br>Finance Service</p>
  <div class="rule"><i></i><i></i></div>
  <p class="call">CALL NOW:-<span class="phone">0800-555-0147</span></p>
  <p class="web">www.<b>corvell</b>.co.uk</p>
  <span class="cta">CLICK HERE<svg><use href="#play"/></svg></span>
  <svg class="arrows" style="right:18px;top:14px;font-size:8px"><use href="#tri-arrows"/></svg>
  <svg class="arrows" style="left:10px;bottom:6px;font-size:7px"><use href="#tri-arrows"/></svg>
</section>

<!-- narrow skyscraper -->
<section class="banner sky-narrow stack">
  <div class="brand"><span class="brand-name">Corvell</span><span class="brand-sub"><b>Finance</b> Limited</span></div>
  <svg class="arrows in-flow" style="align-self:flex-start;margin-left:8px;font-size:7px"><use href="#tri-arrows"/></svg>
  <div class="photo" role="img" aria-label="Photo of a finance adviser with a couple reviewing a laptop"></div>
  <svg class="arrows in-flow" style="align-self:flex-end;margin-right:6px;font-size:6px"><use href="#tri-arrows"/></svg>
  <h2 class="headline">Bridging<br>Loan<br><em>Service</em></h2>
  <p class="pill">5 Star Rated Service<br>&amp; No Broker Fees</p>
  <p class="copy">'Commercial<br>Mortgage<br>Service You Can<br>Rel On' Or<br>'Development<br>Finance Service</p>
  <div class="rule"><i></i><i></i></div>
  <p class="call">CALL NOW:-<span class="phone">0800-555-0147</span></p>
  <p class="web">www.<b>corvell</b>.co.uk</p>
  <span class="cta">CLICK HERE<svg><use href="#play"/></svg></span>
</section>

<!-- wide leaderboard -->
<section class="banner leader-lg strip">
  <div class="brand"><span class="brand-name">Corvell</span><span class="brand-sub"><b>Finance</b> Limited</span></div>
  <div class="photo" role="img" aria-label="Photo of a finance adviser with a couple reviewing a laptop"></div>
  <div class="text">
    <h2 class="headline">Bridging Loan <em>Service</em></h2>
    <p class="pill">5 Star Rated Service &amp; No Broker Fees</p>
    <p class="copy">'Commercial Mortgage Service You Can Rel On' Or 'Development Finance Service</p>
    <div class="rule"><i></i><i></i></div>
    <p class="web">www.<b>corvell</b>.co.uk <span class="cta" style="font-size:.5em;letter-spacing:.1em;margin-left:2em">CLICK HERE<svg><use href="#play"/></svg></span></p>
  </div>
  <p class="call">CALL NOW:-<span class="phone">0800-555-0147</span></p>
  <svg class="arrows" style="left:54px;bottom:8px;font-size:6px"><use href="#tri-arrows"/></svg>
  <svg class="arrows" style="left:193px;top:9px;font-size:6px"><use href="#tri-arrows"/></svg>
  <svg class="arrows" style="right:70px;bottom:15px;font-size:6px"><use href="#tri-arrows"/></svg>
</section>

<!-- leaderboard -->
<section class="banner leader-md strip">
  <div class="brand"><span class="brand-name">Corvell</span><span class="brand-sub"><b>Finance</b> Limited</span></div>
  <div class="photo" role="img" aria-label="Photo of a finance adviser with a couple reviewing a laptop"></div>
  <div class="text">
    <h2 class="headline">Bridging Loan <em>Service</em></h2>
    <p class="pill">5 Star Rated Service &amp; No Broker Fees</p>
    <p class="copy">'Commercial Mortgage Service You Can Rel On' Or 'Development Finance Service</p>
    <p class="web">www.<b>corvell</b>.co.uk <span class="cta" style="font-size:.5em;letter-spacing:.1em;margin-left:2em">CLICK HERE<svg><use href="#play"/></svg></span></p>
  </div>
  <p class="call">CALL NOW:-<span class="phone">0800-555-0147</span></p>
  <svg class="arrows" style="left:26px;bottom:5px;font-size:4px"><use href="#tri-arrows"/></svg>
  <svg class="arrows" style="left:96px;top:5px;font-size:4px"><use href="#tri-arrows"/></svg>
</section>

</body>
</html>
```